Business Card Design Project

we need a business card design for our company: www.dravonix.ch
It's important to include our already existing logo (see website)

```html
<!DOCTYPE html>
<html lang="en">
<head>
<meta charset="utf-8">
<title>Dravonix Business Card</title>
<link rel="stylesheet" href="https://fonts.googleapis.com/css2?family=Exo+2:wght@300;400;500;700&display=swap">
<style>
  :root {
    --bg: #e4e4e4;
    --black: #050505;
    --white: #ffffff;
    --blue: #6fbcf4;
    --blue-deep: #3d9be6;
    --ink: #111111;
  }
  * { margin: 0; padding: 0; box-sizing: border-box; }
  html, body { width: 1200px; height: 900px; overflow: hidden; background: var(--bg); }
  body { position: relative; font-family: "Exo 2", sans-serif; color: var(--ink); }

  .card { position: absolute; border-radius: 26px; overflow: hidden; }

  .card-front { left: 32px; top: 32px; width: 718px; height: 400px; background: var(--white); }
  .front-shape { position: absolute; inset: 0; }
  .edge-stripe { position: absolute; right: 0; top: 48px; width: 12px; bottom: 0; background: var(--blue); }

  .brand-name {
    position: absolute; left: 38px; top: 126px;
    font-size: 46px; font-weight: 700; color: var(--blue-deep); letter-spacing: -0.5px;
  }

  .person { position: absolute; right: 42px; top: 66px; text-align: right; }
  .person-name { font-size: 34px; font-weight: 700; line-height: 1; }
  .person-role { font-size: 17px; font-weight: 400; margin-top: 4px; }

  .contact { position: absolute; font-size: 16px; font-weight: 500; }
  .contact-row { display: flex; align-items: center; gap: 8px; height: 24px; }
  .contact-row svg { width: 16px; height: 16px; flex: none; }
  .contact-phones { left: 372px; top: 190px; }
  .contact-web { left: 476px; top: 266px; }

  .company { position: absolute; left: 298px; top: 346px; padding-left: 12px; border-left: 3px solid var(--blue); }
  .company-name { font-size: 18px; font-weight: 700; line-height: 1.2; }
  .company-address { font-size: 16px; font-weight: 400; line-height: 1.3; }

  .card-back { left: 466px; top: 464px; width: 700px; height: 400px; background: var(--black); }
  .back-line { position: absolute; left: 142px; top: 0; bottom: 0; width: 3px; background: var(--blue); }
  .back-web {
    position: absolute; left: 284px; top: 174px;
    font-size: 36px; font-weight: 300; color: var(--blue); letter-spacing: 0.5px;
  }
</style>
</head>
<body>

<section class="card card-front">
  <svg class="front-shape" viewBox="0 0 718 400" width="718" height="400" aria-hidden="true">
    <path d="M0 0 H312 C262 120 240 290 205 400 H0 Z" fill="var(--black)"/>
    <path d="M312 0 C266 120 256 290 238 400 H205 C240 290 262 120 312 0 Z" fill="var(--blue)"/>
  </svg>
  <div class="edge-stripe"></div>

  <div class="brand-name">Dravonix</div>

  <div class="person">
    <div class="person-name">Lena Marti</div>
    <div class="person-role">Manager</div>
  </div>

  <div class="contact contact-phones">
    <div class="contact-row">
      <svg viewBox="0 0 16 16"><rect x="4" y="1" width="8" height="14" rx="1.5" fill="none" stroke="var(--blue-deep)" stroke-width="1.6"/><line x1="7" y1="12.5" x2="9" y2="12.5" stroke="var(--blue-deep)" stroke-width="1.4"/></svg>
      <span>+41.79.512.7430</span>
    </div>
    <div class="contact-row">
      <svg viewBox="0 0 16 16"><path d="M3 1.5 L6 1.5 L7 5 L5.2 6.3 C6 8.3 7.7 10 9.7 10.8 L11 9 L14.5 10 L14.5 13 C14.5 14 13.6 14.6 12.6 14.5 C7 13.8 2.2 9 1.5 3.4 C1.4 2.4 2 1.5 3 1.5 Z" fill="var(--blue-deep)"/></svg>
      <span>+41.44.730.1100</span>
    </div>
  </div>

  <div class="contact contact-web">
    <div class="contact-row">
      <svg viewBox="0 0 16 16"><rect x="1.5" y="3.5" width="13" height="9" fill="none" stroke="var(--blue-deep)" stroke-width="1.3"/><path d="M1.5 3.5 L8 9 L14.5 3.5" fill="none" stroke="var(--blue-deep)" stroke-width="1.3"/></svg>
      <span>info@dravonix.ch</span>
    </div>
    <div class="contact-row">
      <svg viewBox="0 0 16 16"><circle cx="8" cy="8" r="6.5" fill="none" stroke="var(--blue-deep)" stroke-width="1.3"/><ellipse cx="8" cy="8" rx="3" ry="6.5" fill="none" stroke="var(--blue-deep)" stroke-width="1.1"/><line x1="1.5" y1="8" x2="14.5" y2="8" stroke="var(--blue-deep)" stroke-width="1.1"/></svg>
      <span>www.dravonix.ch</span>
    </div>
  </div>

  <div class="company">
    <div class="company-name">Dravonix AG</div>
    <div class="company-address">Lindenweg 12 - 8005 Zürich</div>
  </div>
</section>

<section class="card card-back">
  <div class="back-line"></div>
  <div class="back-web">www.dravonix.ch</div>
</section>

</body>
</html>
```